Verdant Labs' Verdant Bulk Builder 2500

Verdant Labs supplies Health supplements and have been trading since 1975, mainly to Bodybuilders and weightlifters. Over the years our customers have aged and our range extended to compliment their needs, i.e; more general supplements. However this label is for our Verdant Builder 2500. If you look online you will see this product is in a 3ltr white pot the label currently, is a dark brown background label with red and white lettering, red denoted the flavour of strawberry.
We would like the design to look good and more up to date for both men and women. A white background, with no horizontal lines top and bottom.

```html
<!DOCTYPE html>
<html lang="en">
<head>
<meta charset="utf-8">
<title>Verdant Labs – Verdant Bulk Builder 2500 Label</title>
<link rel="stylesheet" href="https://fonts.googleapis.com/css2?family=Rajdhani:wght@500;600;700&family=Russo+One&family=Righteous&display=swap">
<style>
  :root {
    --page: #ffffff;
    --label-bg: #ffffff;
    --label-edge: #d9d9db;
    --ink: #0d0d0d;
    --red: #d41b24;
    --red-deep: #a81a2a;
    --grey-band: #898a8e;
    --white: #ffffff;
  }
  html, body {
    margin: 0;
    padding: 0;
    width: 1200px;
    height: 897px;
    overflow: hidden;
    background: var(--page);
  }
  .label {
    position: absolute;
    left: 30px;
    top: 166px;
    width: 1140px;
    height: 564px;
    box-shadow: 2px 4px 12px rgba(0,0,0,0.18);
  }
  .label svg { display: block; width: 100%; height: 100%; }
  .brand-name { font-family: "Rajdhani", sans-serif; font-weight: 700; fill: var(--ink); }
  .range-word { font-family: "Righteous", sans-serif; fill: var(--white); letter-spacing: 14px; }
  .product-word { font-family: "Russo One", sans-serif; fill: var(--ink); }
  .strength { font-family: "Righteous", sans-serif; fill: var(--red); stroke: var(--white); stroke-width: 4; paint-order: stroke; }
  .body-copy { font-family: "Rajdhani", sans-serif; font-weight: 500; fill: #333; }
  .growth { font-family: "Russo One", sans-serif; fill: var(--red); }
  .ingredient { font-family: "Rajdhani", sans-serif; font-weight: 600; fill: var(--ink); }
  .benefits-title { font-family: "Rajdhani", sans-serif; font-weight: 700; fill: var(--red); }
  .benefits-copy { font-family: "Rajdhani", sans-serif; font-weight: 600; fill: var(--white); }
  .flavour { font-family: "Rajdhani", sans-serif; font-weight: 600; fill: var(--white); }
  .weight { font-family: "Rajdhani", sans-serif; font-weight: 700; fill: var(--red); }
  .best-before { font-family: "Rajdhani", sans-serif; font-weight: 700; fill: var(--white); }
</style>
</head>
<body>
<div class="label">
  <svg viewBox="0 0 1422 703" xmlns="http://www.w3.org/2000/svg">
    <!-- label body -->
    <rect x="0.5" y="0.5" width="1421" height="702" fill="var(--label-bg)" stroke="var(--label-edge)"/>

    <!-- brand name -->
    <text class="brand-name" x="796" y="95" font-size="58" text-anchor="middle">VERDANT LABS</text>
    <rect x="626" y="106" width="120" height="2" fill="var(--red)"/>

    <!-- grey band behind product name -->
    <g transform="rotate(-4 644 390)">
      <rect x="140" y="330" width="1010" height="125" rx="20" fill="var(--grey-band)"/>
    </g>

    <!-- red splash artwork -->
    <ellipse cx="225" cy="270" rx="110" ry="120" fill="var(--red)" role="img" aria-label="Red paint splash artwork"/>

    <!-- range banner -->
    <polygon points="218,165 742,122 748,178 260,215" fill="var(--red)"/>
    <text class="range-word" x="375" y="195" font-size="56" transform="rotate(-4 375 195)">VERDANT</text>

    <!-- product name -->
    <text class="product-word" x="372" y="322" font-size="150" textLength="450" lengthAdjust="spacingAndGlyphs" transform="rotate(-4 372 322)">BULK</text>
    <text class="product-word" x="452" y="442" font-size="128" textLength="330" lengthAdjust="spacingAndGlyphs" transform="rotate(-4 452 442)">BUILDER</text>

    <!-- strength -->
    <text class="strength" x="762" y="519" font-size="170" textLength="372" lengthAdjust="spacingAndGlyphs">2500</text>

    <!-- description -->
    <rect x="862" y="212" width="3" height="76" fill="var(--red)"/>
    <text class="body-copy" font-size="14">
      <tspan x="877" y="230">Perfect for bodybuilders &amp; sportspeople who wish to gain hard,</tspan>
      <tspan x="877" y="246">lean muscle weight. Very low in fat &amp; high in energy producing</tspan>
      <tspan x="877" y="262">carbohydrates which will enable you to train harder,</tspan>
      <tspan x="877" y="278">longer and grow faster.</tspan>
    </text>

    <!-- growth factors -->
    <text class="growth" font-size="19">
      <tspan x="1144" y="453" letter-spacing="3">CONTAINS</tspan>
      <tspan x="1144" y="469" font-size="17">ALL ESSENTIAL</tspan>
      <tspan x="1144" y="485" font-size="14">GROWTH FACTORS</tspan>
    </text>

    <!-- flavour panel -->
    <rect x="30" y="569" width="925" height="110" rx="14" fill="var(--red-deep)"/>
    <rect x="943" y="627" width="449" height="52" rx="10" fill="var(--red)"/>

    <!-- ingredients -->
    <g class="ingredients">
      <rect x="1167" y="512" width="8" height="8" fill="var(--red)"/>
      <rect x="1167" y="531" width="8" height="8" fill="var(--red)"/>
      <rect x="1167" y="550" width="8" height="8" fill="var(--red)"/>
      <rect x="1167" y="569" width="8" height="8" fill="var(--red)"/>
      <rect x="1167" y="588" width="8" height="8" fill="var(--red)"/>
      <text class="ingredient" font-size="17">
        <tspan x="1181" y="521">GAMMA ORYZANOL</tspan>
        <tspan x="1181" y="540">SELENIUM</tspan>
        <tspan x="1181" y="559">OLYSACCHARIDES</tspan>
        <tspan x="1181" y="578">CHROMIUM POLYNICOTINA</tspan>
        <tspan x="1181" y="597">GTF</tspan>
      </text>
    </g>

    <!-- benefits -->
    <text class="benefits-title" x="282" y="527" font-size="32" transform="rotate(-2 282 527)">BENEFITS</text>
    <g transform="rotate(-3 387 610)">
      <rect x="232" y="540" width="310" height="145" rx="8" fill="var(--ink)"/>
      <text class="benefits-copy" font-size="13">
        <tspan x="248" y="563">-Perfect for people who find it difficult to gain hard,</tspan>
        <tspan x="254" y="579">lean muscle weight</tspan>
        <tspan x="248" y="595">-Bodybuilders &amp; Weight Trainers</tspan>
        <tspan x="248" y="611">-Convalescents</tspan>
        <tspan x="248" y="627">-Very low in fat</tspan>
        <tspan x="248" y="643">-High in energy producing carbohydrates.</tspan>
        <tspan x="248" y="659">-Delicious</tspan>
      </text>
    </g>

    <!-- flavour -->
    <text class="flavour" x="793" y="619" font-size="44" text-anchor="middle">STRAWBERRY</text>
    <text class="flavour" x="793" y="651" font-size="34" text-anchor="middle">flavour</text>

    <!-- net weight -->
    <text class="weight" x="985" y="598" font-size="42">2000g ℮</text>

    <!-- best before -->
    <text class="best-before" x="958" y="660" font-size="20">BEST BEFORE  SEE SIDE OF LABEL   OR THE BASE</text>
  </svg>
</div>
</body>
</html>
```